Kelbrook Training Australia - Course Brochure Design

Kelbrook Training Australia is a Private Register Training Organisation that delivery accredited training courses to students. These courses are delivery via face to face training and distance education (e.g. elearning).

We are looking to get a template designed via adobe in design that we can use for each of our courses and list the information relevant for each one.

It will need to be around 3 - 4 pages long to be able to fit the information required into the brochure, i have attached some example of other providers course information sheets.

From the examples you'll be able to see that most of the information will remained the same until it gets to the course structure.

I would like it to be kept within our current theme, we are in the middle of upgrading our new website and look (www.kelbrook.com.au/drupal).

I look forward to see what you all come back with.

Reason: Hi everyone, Thanks for submitting your design, I have extended the deadline due to not many designs have been submitted. I will be review and providing feedback on the designed submitted this week and will provide some more information based off the work and direction of the designs submitted. Thanks, Ralph.

Target Market(s)

our target market is business and individuals who would like to undergo training course. This brochure needs to display the require information.

Industry/Entity Type

Education

Requirements
Must have
• The brochure must have a front page with a design to list our company logo and information and the course title.

A call to action must be on every page, e.g. footer to enrol now call kelbok on 1800 392 508 or visit www.kelbrook.com.au

Nice to have
• Some picture to fill the pages would add a nice look

```html
<!DOCTYPE html>
<html lang="en">
<head>
<meta charset="utf-8">
<title>Kelbrook Training Australia – Course Brochure</title>
<link rel="stylesheet" href="https://fonts.googleapis.com/css2?family=Arimo:wght@400;700&family=Fira+Sans:wght@500;700&display=swap">
<style>
:root{
  --maroon:#7b1b0d;
  --ink:#4a4a4a;
  --grey:#6d6e70;
  --panel:#e8e8e8;
  --paper:#ffffff;
  --stage:#ffffff;
  --rule:#a33a25;
}
*{box-sizing:border-box;margin:0;padding:0}
html,body{width:1200px;height:960px;overflow:hidden;background:var(--stage)}
body{position:relative;font-family:"Arimo",Arial,sans-serif;color:var(--ink)}
.page{position:absolute;top:90px;width:550px;height:780px;background:var(--paper);
  border:1px solid #d6d6d6;box-shadow:3px 4px 6px rgba(0,0,0,.18);overflow:hidden}
.page--services{left:30px}
.page--solutions{left:620px}
.brand{position:absolute;right:22px;top:40px;display:flex;align-items:center;gap:6px;
  font-family:"Arimo",Arial,sans-serif;font-size:20px;color:var(--maroon)}
.brand__mark{width:10px;height:10px;background:var(--maroon)}
.page-title{position:absolute;left:48px;top:78px;font-family:"Fira Sans",Arial,sans-serif;
  font-weight:500;font-size:23px;color:var(--maroon)}
.col{position:absolute;font-size:7.6px;line-height:12px}
.col p{margin-bottom:6px}
.col ul{list-style:none;margin-bottom:6px}
.col li{padding-left:10px;position:relative}
.col li::before{content:"";position:absolute;left:1px;top:4.5px;width:3.5px;height:3.5px;border-radius:50%;background:var(--ink)}
.section-head{position:absolute;left:48px;width:454px;font-family:"Fira Sans",Arial,sans-serif;
  font-weight:700;font-size:10.5px;color:var(--maroon);padding-bottom:3px;border-bottom:1px solid var(--rule)}
.sub-head{font-family:"Fira Sans",Arial,sans-serif;font-weight:700;font-size:9px;color:#333;margin:4px 0 5px}
.sub-head--italic{font-style:italic;color:var(--maroon);font-size:8px;margin:0}
.note{background:var(--panel);padding:8px 10px;margin:8px 0 10px}
.headline{position:absolute;font-family:"Fira Sans",Arial,sans-serif;font-weight:700;color:var(--maroon);font-size:25px;letter-spacing:.2px}
.headline--one{left:48px;top:140px}
.headline--two{left:148px;top:167px}
.course-head{font-family:"Fira Sans",Arial,sans-serif;font-weight:700;font-size:10px;color:var(--maroon);margin-bottom:6px}
.photo{position:absolute;left:0;top:423px;width:266px;height:193px;
  background:linear-gradient(135deg,#c9bfb3 0%,#8d8478 45%,#3b3a3e 100%)}
.cta{position:absolute;left:0;top:726px;width:550px;height:54px}
.cta__text{position:absolute;right:48px;color:#fff;font-size:10px;text-align:right}
.cta__lead{top:6px}
.cta__contact{top:30px}
.cta__contact b{font-weight:700}
</style>
</head>
<body>

<section class="page page--services">
  <div class="brand"><span class="brand__mark"></span>kelbrook</div>
  <h1 class="page-title">Our services</h1>

  <h2 class="section-head" style="top:139px">Corporate Training</h2>
  <div class="col" style="left:48px;top:160px;width:226px">
    <p>Kelbrook does not deliver ‘standard’ corporate training programs; all of our content has been developed specifically to meet the needs of a wide range of corporate clients and the common trouble areas.</p>
    <p>With over twenty three years of delivering quality training to corporate clients, our training materials have been updated throughout the years to better impact the problem areas that many private corporate companies face.</p>
    <p>Our corporate training programs are listed below in brief and more details can be found on our website:</p>
    <ul><li>Interpersonal skills</li><li>Managing time for results</li></ul>
  </div>
  <div class="col" style="left:284px;top:161px;width:220px">
    <ul>
      <li>Leading and developing teams</li><li>Training small groups</li><li>Client services</li>
      <li>How to get a job</li><li>Life and career management</li><li>Active listening skills</li>
      <li>Conflict resolution skills</li><li>Leadership and change</li><li>Foundation of management</li>
      <li>Frontline management course</li><li>Presentation skills</li><li>Workplace assessment units</li>
      <li>Fire training</li>
    </ul>
  </div>

  <h2 class="section-head" style="top:333px">Traineeships</h2>
  <div class="col" style="left:48px;top:355px;width:228px">
    <p>An Apprenticeship/Traineeship is an opportunity for someone that works part-time or full-time to undergo a structured training program to achieve a Nationally Recognised Qualification.</p>
    <p>All of our traineeships Qualifications are offered using the latest National Training Packages and training resources. As with all of our training, these packages can be accessed through the following methods:</p>
    <ul><li>Traditional classroom environment</li><li>One-to-one in the workplace</li><li>Group training in the workplace</li><li>Online</li></ul>
    <p>And if our standard delivery methods don’t meet your requirements, we can personalise a training method that best suits your company.</p>
    <p>Traineeships available through Kelbrook Training Australia are:</p>
    <ul>
      <li>Business</li><li>Business Administration</li><li>Customer Contact</li><li>Business Sales</li>
      <li>Frontline Management</li><li>Occupational Health and Safety</li><li>Project Management</li>
      <li>Asset Maintenance</li><li>Hospitality</li><li>Retail</li><li>Transport &amp; Logistics</li><li>Aged Care</li>
    </ul>
  </div>
  <div class="col" style="left:284px;top:355px;width:220px">
    <p>Please contact us to confirm that each state supports the qualification in question.</p>
    <p>As a Registered Training Organisation (RTO), Kelbrook Training Australia is accredited to deliver all Certificates level of a number of the National Training Packages as it applies to User Choice (Traineeships). As a result, we would be able to take care of any training requirements for your staff members. We follow and adhere to all AQTF principles within all our practices.</p>
    <div class="note">Kelbrook is an equal opportunity training service provider, we encourage participation by individuals from all backgrounds including those with physical and/or intellectual disabilities.</div>
    <h3 class="sub-head">Trainee Categories</h3>
    <h4 class="sub-head sub-head--italic">New Entrant</h4>
    <p>An employee that has been employed for LESS than 3 months Full-Time or LESS than 12 months Part-Time or Casual is considered a New Entrant. Trainees that meet the requirements as a “New Entrant” may receive State Government Funded training. In this scenario, the training is subsided by the State Government directly to the Registered Training Organisation (RTO), and the employer needs only to pay an enrolment fee or in some cases an employer contribution which is a mandatory State Government Fee.</p>
  </div>

  <div class="cta">
    <svg width="550" height="54" viewBox="0 0 550 54" aria-hidden="true">
      <polygon points="46,0 550,0 550,20 42,20" fill="var(--maroon)"/>
      <polygon points="40,24 550,24 550,54 34,54" fill="var(--grey)"/>
    </svg>
    <p class="cta__text cta__lead">For more information or to enrol now:</p>
    <p class="cta__text cta__contact">call <b>1800 392 508</b> or visit <b>www.kelbrook.com.au</b></p>
  </div>
</section>

<section class="page page--solutions">
  <div class="brand"><span class="brand__mark"></span>kelbrook</div>
  <h1 class="headline headline--one">FRESH SOLUTIONS</h1>
  <p class="headline headline--two">in training for your business</p>

  <div class="col" style="left:48px;top:234px;width:220px">
    <h2 class="course-head">Training Courses</h2>
    <h3 class="sub-head" style="margin:0">Business</h3>
    <p>There are a range of certificates in the business qualification. They have been designed to be generic, broad based and contextualised for enterprises, regions, localities and groups across the full spectrum of Australian industry. The qualifications provide essential cross industry skills for all business enterprises.</p>
    <p>A diverse range of courses taking you from using basic business technology, running meetings, working with a team, self -directional planning and working, safe working and record management, through to preparing risk analyses, creating and optimizing team output and executing business operational and financial plans.</p>
  </div>

  <div class="photo" role="img" aria-label="Photo of a smiling business team in office wear holding a folder"></div>

  <div class="col" style="left:48px;top:642px;width:220px">
    <h3 class="sub-head" style="margin:0">Business Administration</h3>
    <p>These courses are designed to support your career path from working within a busy business office environment providing administration support, to supervising a team to ensure smooth and efficient running of the working team.</p>
  </div>

  <div class="col" style="left:284px;top:253px;width:220px">
    <p>You may be, or want to be, administration support, a personal assistant, an accounts manager, project supervisor or manager, the list is endless. The units are selected and tailored to suit the needs of your particular work environment and own aspirations.</p>
    <p>In certificate III level the units include general administrative and IT competencies, such as word processing, keyboarding, scheduling and using a range of software packages to produce documents and databases.</p>
    <p>The Certificate IV is designed for people working in roles such as administration officer, accounts supervisor or executive personal assistant roles.</p>
    <h3 class="sub-head" style="margin:6px 0 0">Customer Contact</h3>
    <p>These courses are designed with current or potential customer service representatives, call/contact centre agents or telesales representatives, as well as more senior customer service representatives.</p>
    <p>Content and delivery is tailored to the working environment and to optimize your current and desired customer contact skills.</p>
    <p>These courses can also support working environments that have not necessarily traditionally been seen as a strict customer contact role such as door guards, airport and other security personnel. Anywhere that you are likely to deal with customers, clients or the public will benefit from these courses.</p>
    <p>Units of competency covered in these qualifications could include safe innovative working, meeting internal and external customer requirements, increasing quality output and resolving customer complaints, working effectively in a customer contact environment and actioning customer contact.</p>
    <p>The Certificate IV qualification has been designed for roles such as analysts, quality assurance officers, schedulers, subject matter expert/coaches and team leaders.</p>
  </div>

  <div class="cta">
    <svg width="550" height="54" viewBox="0 0 550 54" aria-hidden="true">
      <polygon points="46,0 550,0 550,20 42,20" fill="var(--maroon)"/>
      <polygon points="40,24 550,24 550,54 34,54" fill="var(--grey)"/>
    </svg>
    <p class="cta__text cta__lead">For more information or to enrol now:</p>
    <p class="cta__text cta__contact">call <b>1800 392 508</b> or visit <b>www.kelbrook.com.au</b></p>
  </div>
</section>

</body>
</html>
```